Tallow & Mersey Needs New Stationery / Letterhead Design

We need new stationery to match our new logo (attached). Tallow & Mersey is a 34 year old nationwide law firm located in Houston Tx. They do personal injury law and pharmaceutical litigation.

WE DO NOT NEED BUSINESS CARDS.

Attached are several different file formats of the new logo.

Reason: We will make a decision in the next couple days. Finalizing edits now. Thank you!

Target Market(s)

consumers who have been injured due to the negligence of another or by a pharmaceutical drug or defective medical device. Also co-counsel and opposing counsel (law firms0.

Industry/Entity Type

Law Firm

Requirements
Must have
• logo
• Tallow & Mersey, LLP
• 7183 Corvid Lane, Suite 1000
• Brenford, TX 75591
• Tel: (555) 408-1936
• Fax: (555) 408-2275
• www.tallowandmersey.example
• Must have colors in the logo.
• Make the font go with the logo - not necessarily the same, but something that goes well with it.

```html
<!DOCTYPE html>
<html lang="en">
<head>
<meta charset="utf-8">
<title>Tallow &amp; Mersey Stationery</title>
<link rel="stylesheet" href="https://fonts.googleapis.com/css2?family=Raleway:wght@400;600&display=swap">
<style>
:root{
  --stage:#5f5f5f;
  --paper:#ffffff;
  --navy:#1b3d66;
  --ink:#8a8f96;
  --flap-shadow:#e9e9ea;
}
*{margin:0;padding:0;box-sizing:border-box}
html,body{width:1057px;height:1200px;overflow:hidden}
body{background:var(--stage);position:relative;font-family:"Raleway",sans-serif;color:var(--ink)}
.sheet,.card,.envelope{position:absolute;background:var(--paper);overflow:hidden}
.icon{width:13px;height:13px;fill:var(--navy);flex:none}
.contact{display:flex;align-items:center;gap:5px;font-size:10px;white-space:nowrap}
.contact-row{position:absolute;display:flex;gap:14px}

/* wordmark */
.wordmark{position:absolute;display:flex;align-items:center;gap:8px;color:var(--navy);font-weight:600;white-space:nowrap}
.wordmark .mark{background:var(--navy);flex:none}

/* letterhead */
.letterhead{left:243px;top:20px;width:643px;height:902px}
.letterhead .wordmark{left:26px;top:74px;font-size:19px}
.letterhead .wordmark .mark{width:24px;height:24px}
.letterhead .rule{position:absolute;left:26px;top:113px;width:592px;height:2px;background:var(--navy)}
.letterhead .address{right:25px;top:94px}
.letterhead .phones{left:372px;top:119px}
.letterhead .web{position:absolute;right:24px;top:857px}
.letterhead .foot-band{position:absolute;left:0;bottom:0;width:100%;height:23px;background:var(--navy)}

/* card */
.card{left:28px;top:943px;width:494px;height:232px;border-radius:12px}
.card .band{position:absolute;left:0;top:39px;width:100%;height:28px;background:var(--navy)}
.card .logo-plate{position:absolute;left:31px;top:22px;width:176px;height:52px;background:var(--paper)}
.card .wordmark{left:38px;top:40px;font-size:14px;gap:6px}
.card .wordmark .mark{width:18px;height:18px}

/* envelope */
.envelope{left:537px;top:943px;width:494px;height:232px;border-radius:12px}
.envelope .flap{position:absolute;left:0;top:0}
.envelope .address{right:10px;top:180px;position:absolute}
.envelope .rule{position:absolute;left:6px;top:197px;width:482px;height:2px;background:var(--navy)}
.envelope .web{position:absolute;left:6px;top:205px}
.envelope .phones{left:200px;top:205px}
</style>
</head>
<body>

<svg width="0" height="0" style="position:absolute" aria-hidden="true">
  <symbol id="i-pin" viewBox="0 0 24 24"><path d="M12 1a8 8 0 0 0-8 8c0 6 8 14 8 14s8-8 8-14a8 8 0 0 0-8-8zm0 11a3 3 0 1 1 0-6 3 3 0 0 1 0 6z"/></symbol>
  <symbol id="i-phone" viewBox="0 0 24 24"><path d="M6.6 10.8a15 15 0 0 0 6.6 6.6l2.2-2.2a1 1 0 0 1 1-.25 11 11 0 0 0 3.6.6 1 1 0 0 1 1 1V20a1 1 0 0 1-1 1A17 17 0 0 1 3 4a1 1 0 0 1 1-1h3.5a1 1 0 0 1 1 1c0 1.25.2 2.450.6 3.6a1 1 0 0 1-.25 1z"/></symbol>
  <symbol id="i-fax" viewBox="0 0 24 24"><path d="M6 2h9l3 3v4H6zM2 10h20v11H2zm3 3v2h3v-2zm5 0v2h3v-2zm5 0v2h4v-2zM5 17v2h3v-2zm5 0v2h3v-2z"/></symbol>
  <symbol id="i-web" viewBox="0 0 24 24"><path d="M12 20l3-3.5a4.5 4.5 0 0 0-6 0zM5 12.5l2 2.4a7.5 7.5 0 0 1 10 0l2-2.4a10.5 10.5 0 0 0-14 0zM1 8l2 2.4a13.5 13.5 0 0 1 18 0L23 8a16.5 16.5 0 0 0-22 0z"/></symbol>
</svg>

<section class="sheet letterhead" aria-label="Letterhead">
  <div class="wordmark"><span class="mark"></span>Tallow &amp; Mersey</div>
  <div class="rule"></div>
  <div class="contact-row address">
    <span class="contact"><svg class="icon"><use href="#i-pin"/></svg>7183 Corvid Lane, Suite 1000, Brenford, TX 75591</span>
  </div>
  <div class="contact-row phones">
    <span class="contact"><svg class="icon"><use href="#i-phone"/></svg>(555) 408-1936</span>
    <span class="contact"><svg class="icon"><use href="#i-fax"/></svg>(555) 408-2275</span>
  </div>
  <span class="contact web"><svg class="icon"><use href="#i-web"/></svg>www.tallowandmersey.example</span>
  <div class="foot-band"></div>
</section>

<section class="card" aria-label="Compliment card">
  <div class="band"></div>
  <div class="logo-plate"></div>
  <div class="wordmark"><span class="mark"></span>Tallow &amp; Mersey</div>
</section>

<section class="envelope" aria-label="Envelope">
  <svg class="flap" width="494" height="170" viewBox="0 0 494 170" aria-hidden="true">
    <polygon points="0,22 246,166 494,22 494,32 246,170 0,32" fill="var(--flap-shadow)"/>
    <polygon points="0,0 494,0 494,22 246,152 0,22" fill="var(--navy)"/>
  </svg>
  <span class="contact address"><svg class="icon"><use href="#i-pin"/></svg>7183 Corvid Lane, Suite 1000, Brenford, TX 75591</span>
  <div class="rule"></div>
  <span class="contact web"><svg class="icon"><use href="#i-web"/></svg>www.tallowandmersey.example</span>
  <div class="contact-row phones">
    <span class="contact"><svg class="icon"><use href="#i-phone"/></svg>(555) 408-1936</span>
    <span class="contact"><svg class="icon"><use href="#i-fax"/></svg>(555) 408-2275</span>
  </div>
</section>

</body>
</html>
```